PickvaroNow Landing Page

We need a landing page for PickvaroNow, which is a Deal of the day website targeting and providing daily deals to college students. The information we need on the page is as follows:
-The PickvaroNow logo
-Save 50% to 90% on Great Deals Near Your College Campus and Beyond
-Enter Your Information
Email:
Location:
And a Submit button
-The footer
-We’d like to see a reference to how to earn credits for inviting friends: We are offering $50 Journexa gift card for 10 new invites or $5 PickvaroNow dollars for each invite.
If you visit www.pickvaronow.example/marketing you can see our current landing page with all of the information. If you have any questions, please contact Marisol at MBrottweiler@pickvaronow.example
Updates
We will need a Photoshop version of the final design as well.
PickvaroNow has made a change to their target market, and is no longer just targeting college students. We are expanding our target market ages: 18-50+. The majority of our members will be between the ages of 18-35, so please keep that in mind when you are editing your designs. I am very sorry for the inconvenience. I will be extending the end date so there is enough time to edit. Thank you and keep up the great work!

```html
<!DOCTYPE html>
<html lang="en">
<head>
<meta charset="utf-8">
<title>PickvaroNow – Save 50% to 90% on Great Deals</title>
<link href="https://fonts.googleapis.com/css2?family=Gochi+Hand&family=Arimo:wght@400;700&display=swap" rel="stylesheet">
<style>
  :root {
    --paper: #ececec;
    --paper-light: #f4f4f4;
    --navy: #1f3c4f;
    --green: #8db03c;
    --green-light: #a8c85a;
    --green-deep: #6e9426;
    --ink: #1d3344;
    --white: #ffffff;
    --partner-top: #2f5f9e;
    --partner-bottom: #183b72;
  }
  * { box-sizing: border-box; margin: 0; padding: 0; }
  html, body { width: 1200px; height: 786px; overflow: hidden; }
  body {
    position: relative;
    background: var(--paper);
    font-family: "Arimo", Arial, sans-serif;
    color: var(--ink);
  }
  .hero-band { position: absolute; left: 0; top: 0; width: 1200px; height: 666px; }

  .brand-name {
    font-family: "Arimo", Arial, sans-serif;
    font-weight: 700;
    line-height: 1;
    color: var(--navy);
    white-space: nowrap;
  }
  .site-brand { position: absolute; left: 84px; top: 34px; }
  .site-brand .brand-name { font-size: 54px; letter-spacing: -1px; }

  .headline {
    position: absolute; left: 94px; top: 214px;
    font-family: "Gochi Hand", cursive;
    color: var(--white);
    white-space: nowrap;
  }
  .headline h1 { font-size: 42px; font-weight: 400; line-height: 50px; }
  .headline h2 { font-size: 31px; font-weight: 400; line-height: 36px; margin-top: 2px; }

  .signup { position: absolute; left: 94px; top: 320px; width: 240px; }
  .signup-title { font-weight: 700; font-size: 19px; color: var(--green); margin-bottom: 15px; }
  .field {
    display: block; width: 238px; height: 40px; margin-bottom: 18px;
    border: 3px solid #e2e2e2; border-radius: 8px;
    background: var(--white);
    font: 17px "Arimo", Arial, sans-serif; color: #222;
    padding: 0 10px; line-height: 34px;
    box-shadow: inset 0 1px 3px rgba(0,0,0,.25);
    position: relative;
  }
  .field-select::after {
    content: "▴\A▾"; white-space: pre; position: absolute; right: 10px; top: 8px;
    font-size: 8px; line-height: 9px; color: #222;
  }
  .submit {
    display: block; width: 121px; height: 35px; border: 0; border-radius: 18px;
    background: linear-gradient(var(--green-light), var(--green-deep));
    color: var(--white); font-family: "Gochi Hand", cursive; font-size: 21px;
    box-shadow: 0 2px 3px rgba(0,0,0,.35);
  }

  .rewards { position: absolute; left: 101px; top: 542px; display: flex; gap: 11px; }
  .reward { width: 112px; }
  .reward-card {
    height: 66px; border: 4px solid #e9e9e9; border-radius: 5px; position: relative;
    font-weight: 700; color: var(--white);
  }
  .reward-card--partner { background: linear-gradient(var(--partner-top), var(--partner-bottom)); }
  .reward-card--house { background: linear-gradient(135deg, #9bbb4c 0 40%, #f4f4f4 40%); }
  .reward-amount { position: absolute; font-size: 16px; }
  .reward-card--partner .reward-amount { right: 8px; bottom: 8px; }
  .reward-card--house .reward-amount { left: 6px; top: 5px; font-size: 13px; }
  .reward-label { position: absolute; font-size: 9px; }
  .reward-card--partner .reward-label { right: 6px; top: 6px; }
  .reward-card--house .reward-label { right: 6px; bottom: 10px; color: var(--navy); }
  .reward-note { margin-top: 5px; font-size: 9px; color: var(--white); }

  .hero-photo {
    position: absolute; left: 546px; top: 274px; width: 510px; height: 380px;
    background: radial-gradient(ellipse at 50% 55%, #c9b79a 0%, #8ba65a 45%, #3e6a86 80%, rgba(42,81,102,0) 100%);
    border-radius: 200px 200px 0 0;
  }

  .site-footer {
    position: absolute; left: 0; top: 654px; width: 1200px; height: 132px;
    border-top: 12px solid var(--green); background: var(--paper-light);
  }
  .footer-links { position: absolute; top: 34px; list-style: none; font-size: 14.5px; line-height: 17.4px; color: var(--ink); }
  .footer-social { position: absolute; left: 697px; top: 34px; list-style: none; font-size: 14.5px; }
  .footer-social li { display: flex; align-items: center; gap: 9px; height: 24px; }
  .social-icon { width: 17px; height: 17px; }
  .footer-brand { position: absolute; left: 934px; top: 30px; width: 182px; text-align: right; }
  .footer-brand .brand-name { font-size: 29px; letter-spacing: -0.5px; text-align: left; }
  .copyright { margin-top: 24px; font-size: 14px; }
</style>
</head>
<body>
  <svg class="hero-band" viewBox="0 0 1200 666" aria-hidden="true">
    <defs>
      <linearGradient id="bandFill" x1="0" y1="0" x2="0" y2="1">
        <stop offset="0" stop-color="#2c5569"/>
        <stop offset="1" stop-color="#1b3645"/>
      </linearGradient>
    </defs>
    <polygon points="0,192 200,168 222,128 240,165 1200,52 1200,68 240,182 0,214" fill="#8db03c"/>
    <polygon points="0,214 240,182 1200,68 1200,654 0,654" fill="url(#bandFill)"/>
  </svg>

  <header class="site-brand">
    <div class="brand-name">PickvaroNow</div>
  </header>

  <div class="headline">
    <h1>Save 50% to 90% on Great Deals</h1>
    <h2>Near Your College Campus and Beyond</h2>
  </div>

  <form class="signup">
    <p class="signup-title">Enter Your Information</p>
    <div class="field">Email</div>
    <div class="field field-select">select location</div>
    <button class="submit" type="button">SUBMIT</button>
  </form>

  <div class="rewards">
    <div class="reward">
      <div class="reward-card reward-card--partner">
        <span class="reward-label">Journexa</span>
        <span class="reward-amount">$50</span>
      </div>
      <p class="reward-note">*for 10 new invites</p>
    </div>
    <div class="reward">
      <div class="reward-card reward-card--house">
        <span class="reward-amount">$5</span>
        <span class="reward-label">PickvaroNow</span>
      </div>
      <p class="reward-note">*for each invite</p>
    </div>
  </div>

  <div class="hero-photo" role="img" aria-label="Photo of two smiling young friends sitting together holding coffee mugs"></div>

  <footer class="site-footer">
    <ul class="footer-links" style="left:84px"><li>Daily Deal</li><li>Recent Deals</li><li>How It Works</li><li>Submit Business</li></ul>
    <ul class="footer-links" style="left:229px"><li>Feedback</li><li>Sign Up</li><li>Feature Your Business</li></ul>
    <ul class="footer-links" style="left:421px"><li>FAQs</li><li>About Us</li><li>Contact Us</li></ul>
    <ul class="footer-links" style="left:553px"><li>Legal</li><li>Our Promise</li><li>We're Hiring</li></ul>
    <ul class="footer-social">
      <li><svg class="social-icon" viewBox="0 0 17 17"><rect x="1" y="3" width="15" height="11" fill="#f2f2f2" stroke="#999"/><path d="M1 3 L8.5 9 L16 3" fill="none" stroke="#999"/></svg>Contact us via Email</li>
      <li><svg class="social-icon" viewBox="0 0 17 17"><rect width="17" height="17" rx="2" fill="#3b5b98"/></svg>Join on Friendspace</li>
      <li><svg class="social-icon" viewBox="0 0 17 17"><rect width="17" height="17" rx="2" fill="#4fb3d9"/></svg>Follow us on Chirpline</li>
    </ul>
    <div class="footer-brand">
      <div class="brand-name">PickvaroNow</div>
      <p class="copyright">© 2011 | PickvaroNow.</p>
    </div>
  </footer>
</body>
</html>
```